Tradeshow Banner Design (Qty2, 6'H x 2'W)

Brightwell Contractors is an Electrical, Fire Alarm, and Security Contracting company. For tradeshows, we would like 2 vertical Banners to put behind our booth. Our colors are Red, Grey & Black. I would like the Banners to be informative on what services we provide, with some appealing Graphic Design. (bwc-kmo.com)
Slogan: Safeguarding Communities Electrical, Fire & Security Solutions
Target Market(s)
Commercial Construction Clients
Industry/Entity Type
Electrical / Construction
Font styles to use
Other font styles liked:
- Aileron
Colors
EB3D1F
EC4F4E
F09395
F8D3D4
FCEDEE
Requirements
Must have
- Our Logo, Color Scheme, Brief Caption of the services we provide
Nice to have
- Appealing Imagery & a modern/simplistic design

```html
<!DOCTYPE html>
<html lang="en">
<head>
<meta charset="utf-8">
<title>Brightwell Contractors – Tradeshow Banners</title>
<link href="https://fonts.googleapis.com/css2?family=Poppins:wght@700;800&family=Roboto:wght@400;500;700&display=swap" rel="stylesheet">
<style>
:root{
  --red:#EB1F24;
  --red-deep:#D8181E;
  --black:#1c1c1c;
  --ink:#2a2a2a;
  --grey:#5a5a5a;
  --stage:#2b2b2b;
  --frame:#2a0f10;
  --white:#ffffff;
  --photo-a:#4a5d78;
  --photo-b:#2f3b2e;
}
*{margin:0;padding:0;box-sizing:border-box}
html,body{width:1200px;height:1200px;overflow:hidden;background:var(--stage)}
body{position:relative;font-family:"Roboto",Arial,sans-serif;color:var(--ink)}
.banner{position:absolute;top:0;width:564px;height:1200px;overflow:hidden;background:var(--white)}
.banner--grid{left:25px}
.banner--pills{left:612px;background:var(--black)}
.abs{position:absolute}
.photo{position:absolute;background:linear-gradient(180deg,var(--photo-a) 0%,#6b6a66 45%,var(--photo-b) 100%)}
.brand{position:absolute;display:flex;align-items:center;gap:10px;z-index:2}
.brand__dot{width:112px;height:112px;border-radius:50%;background:var(--red);flex:none}
.brand__name{font-family:"Roboto",Arial,sans-serif;font-weight:500;color:var(--grey);font-size:27px;line-height:1;letter-spacing:.5px}
.brand__tag{font-size:11px;color:var(--grey);margin-top:6px;letter-spacing:.3px;white-space:nowrap}
.brand--compact{gap:8px}
.brand--compact .brand__dot{width:106px;height:106px}
.brand--compact .brand__name{font-size:22px;letter-spacing:.2px}
.brand--compact .brand__tag{font-size:9.5px;letter-spacing:0;margin-top:5px}
.headline{position:absolute;left:0;width:564px;text-align:center;font-family:"Poppins",Arial,sans-serif;font-weight:800;color:var(--white);font-size:31px;line-height:40px;text-transform:uppercase;text-shadow:0 2px 6px rgba(0,0,0,.55);letter-spacing:.5px}
.feature{position:absolute;left:39px;top:507px;width:486px;height:171px;background:var(--white)}
.feature__title{position:absolute;left:174px;top:14px;font-family:"Roboto",Arial,sans-serif;font-weight:700;color:var(--red);font-size:31px;letter-spacing:-.5px}
.feature__body{position:absolute;left:172px;top:50px;width:298px;font-size:11.6px;line-height:14.2px;text-align:justify}
.card{position:absolute;top:720px;width:162px}
.card__photo{height:143px}
.card__label{height:39px;background:var(--red);color:var(--white);font-family:"Poppins",Arial,sans-serif;font-weight:800;font-size:17px;display:flex;align-items:center;justify-content:center;text-align:center;line-height:15px;letter-spacing:.5px}
.card__label--small{font-size:14px}
.card__body{margin-top:6px;font-size:9.6px;line-height:12.1px;text-align:justify}
.cta{position:absolute;left:0;top:1028px;width:564px;height:66px;background:var(--red);color:var(--white);font-family:"Poppins",Arial,sans-serif;font-weight:800;font-size:27px;line-height:27px;text-align:center;letter-spacing:2px;padding-top:7px}
.contact{position:absolute;left:0;top:1094px;width:564px;height:106px;background:var(--white)}
.contact__slab{position:absolute;left:0;top:0}
.contact__kicker{position:absolute;left:26px;top:20px;font-family:"Poppins",Arial,sans-serif;font-weight:700;font-size:13px;color:var(--ink);letter-spacing:.5px}
.contact__phone{position:absolute;left:24px;top:38px;display:flex;align-items:center;gap:6px;font-family:"Poppins",Arial,sans-serif;font-weight:800;font-size:32px;color:var(--ink);line-height:1}
.contact__mail{position:absolute;left:24px;top:77px;font-family:"Poppins",Arial,sans-serif;font-weight:700;font-size:12.5px;color:var(--ink);letter-spacing:.3px}
.badge-round{position:absolute;left:362px;top:17px;width:72px;height:72px;border-radius:50%;border:3px solid var(--white);background:#3a3a3a}
.badge-square{position:absolute;left:448px;top:17px;width:62px;height:56px;border:5px solid var(--white);border-radius:6px}
.pill{position:absolute;height:88px;background:var(--red);border-radius:26px;box-shadow:4px 5px 0 var(--white);color:var(--white)}
.pill__title{position:absolute;top:9px;font-family:"Poppins",Arial,sans-serif;font-weight:800;font-size:19px;line-height:20px;letter-spacing:1.2px}
.pill__body{position:absolute;top:31px;font-family:"Roboto",Arial,sans-serif;font-weight:500;font-size:9.8px;line-height:10.6px;text-align:justify}
.pill--left .pill__title{left:50px}
.pill--left .pill__body{left:50px;right:14px}
.pill--right .pill__title{right:50px;text-align:right}
.pill--right .pill__body{left:14px;right:50px}
.pill__photo{position:absolute;width:114px;height:114px;border-radius:50%;border:4px solid var(--white);box-shadow:0 0 0 4px var(--red)}
</style>
</head>
<body>

<section class="banner banner--grid">
  <svg class="abs" style="left:0;top:84px" width="564" height="56" viewBox="0 0 564 56"><polygon points="345,1 564,1 564,56 295,56" fill="var(--red)"/></svg>
  <div class="brand brand--compact" style="left:32px;top:18px">
    <div class="brand__dot"></div>
    <div>
      <div class="brand__name">BRIGHTWELL<br>CONTRACTORS</div>
      <div class="brand__tag">ELECTRICAL | FIRE | SECURITY</div>
    </div>
  </div>

  <div class="photo" style="left:0;top:139px;width:564px;height:322px" role="img" aria-label="Modern apartment buildings at dusk with lit windows, a pond and landscaped walkways"></div>
  <h1 class="headline" style="top:214px">Safeguarding<br>communities electrical,<br>fire and security<br>solutions</h1>

  <svg class="abs" style="left:0;top:0" width="564" height="800" viewBox="0 0 564 800">
    <polygon points="0,461 240,461 282,430 324,461 564,461 564,792 0,792" fill="var(--red)"/>
    <polygon points="24,491 248,491 282,462 316,491 540,491 540,692 24,692" fill="var(--frame)"/>
  </svg>
  <div class="feature">
    <div class="photo" style="left:0;top:0;width:140px;height:171px;background:linear-gradient(135deg,#f1f1f1,#e04048 60%,#f3c9a9)" role="img" aria-label="Hand pulling a red fire alarm pull station on a white wall"></div>
    <h2 class="feature__title">FIRE PROTECTION</h2>
    <p class="feature__body">Our commercial fire alarm systems are designed to protect your employees and property. We offer outstanding systems designed to detect fire and life safety emergencies. Our systems provide fire detection, signaling, and control systems that warn of alarm or abnormal conditions, as well as help, notify fire and rescue services.</p>
  </div>

  <article class="card" style="left:24px">
    <div class="card__photo photo" style="position:static;background:linear-gradient(135deg,#f4f4f4,#e6e6e6)" role="img" aria-label="Hand touching a white motion sensor on a wall"></div>
    <h3 class="card__label">SECURITY</h3>
    <p class="card__body">In cases of emergencies, there is no time to waste. For fires and break-ins, you need split-second reaction times. At Brightwell Contractors, we pride ourselves on our lightning-fast reaction times in letting the relevant officials know as soon as one of our alarm systems goes off.</p>
  </article>
  <article class="card" style="left:201px">
    <div class="card__photo photo" style="position:static;background:linear-gradient(135deg,#c9b48a,#5f6f86 55%,#dfe3e8)" role="img" aria-label="Dome security camera in a busy warehouse"></div>
    <h3 class="card__label">SURVEILLANCE</h3>
    <p class="card__body">Owning a business is expensive, and leaving it unattended every night is a huge risk. This is why we at Brightwell Contractors believe that owning one of our CCTV or IP camera systems is a great way to monitor the safety of your business and your staff 24 hours a day.</p>
  </article>
  <article class="card" style="left:378px">
    <div class="card__photo photo" style="position:static;background:linear-gradient(135deg,#8a8f96,#3b3f45 60%,#c9a23c)" role="img" aria-label="Electrician in hard hat working on an electrical panel"></div>
    <h3 class="card__label card__label--small">ELECTRICAL<br>SERVICES</h3>
    <p class="card__body">To remain the one-stop-shop that we strive to be for our customers, Brightwell Contractors Tech has a team of licensed Line Voltage Electricians. This team possess the ability to help our customers with a variety of projects and troubleshooting.</p>
  </article>

  <div class="cta">LET US HELP YOU PROTECT<br>YOUR BUSINESS TODAY.</div>
  <div class="contact">
    <svg class="contact__slab" width="564" height="106" viewBox="0 0 564 106"><polygon points="329,0 564,0 564,106 295,106" fill="var(--black)"/></svg>
    <div class="contact__kicker">CONTACT US</div>
    <div class="contact__phone">
      <svg width="26" height="28" viewBox="0 0 24 24"><path fill="var(--ink)" d="M6.6 10.8a15.1 15.1 0 0 0 6.6 6.6l2.2-2.2c.3-.3.7-.4 1-.2 1.1.4 2.3.6 3.6.6.6 0 1 .4 1 1V20c0 .6-.4 1-1 1A17 17 0 0 1 3 4c0-.6.4-1 1-1h3.5c.6 0 1 .4 1 1 0 1.3.2 2.5.6 3.6.1.3 0 .7-.2 1z"/></svg>
      555-204-7390
    </div>
    <div class="contact__mail">OFFICE@BWC-KMO.COM</div>
    <div class="badge-round"></div>
    <div class="badge-square"></div>
  </div>
</section>

<section class="banner banner--pills">
  <svg class="abs" style="left:0;top:0" width="564" height="560" viewBox="0 0 564 560">
    <rect x="0" y="0" width="564" height="240" fill="var(--white)"/>
    <path d="M0 196 Q270 115 564 216 V230 Q270 135 0 215 Z" fill="var(--red)"/>
    <path d="M0 545 Q300 520 564 545 V560 H0 Z" fill="var(--black)"/>
  </svg>
  <div class="photo" style="left:0;top:150px;width:564px;height:400px;clip-path:path('M0 66 Q270 -12 564 80 L564 347 Q330 290 0 277 Z')" role="img" aria-label="Modern apartment buildings at dusk with lit windows and landscaped grounds"></div>
  <svg class="abs" style="left:0;top:0" width="564" height="560" viewBox="0 0 564 560">
    <path d="M0 427 Q330 440 564 497 V540 Q330 470 0 437 Z" fill="var(--red)"/>
  </svg>
  <div class="brand" style="left:143px;top:17px">
    <div class="brand__dot" style="width:118px;height:118px"></div>
    <div>
      <div class="brand__name" style="font-size:29px">BRIGHTWELL<br>CONTRACTORS</div>
      <div class="brand__tag">ELECTRICAL | FIRE | SECURITY</div>
    </div>
  </div>
  <h1 class="headline" style="top:336px;left:-3px">Safeguarding<br>communities electrical<br>fire and security<br>solutions</h1>

  <article class="pill pill--left" style="left:130px;top:562px;width:378px">
    <h3 class="pill__title">FIRE PROTECTION</h3>
    <p class="pill__body">Our commercial fire alarm systems are designed to protect your employees and property. We offer outstanding systems designed to detect fire and life safety emergencies. Our systems provide fire detection, signaling, and control</p>
  </article>
  <div class="pill__photo" style="left:55px;top:545px;background:linear-gradient(135deg,#f1f1f1,#e04048 60%,#f3c9a9)" role="img" aria-label="Hand pulling a red fire alarm pull station"></div>

  <article class="pill pill--right" style="left:53px;top:674px;width:384px">
    <h3 class="pill__title">SECURITY</h3>
    <p class="pill__body">In cases of emergencies, there is no time to waste. For fires and break-ins, you need split-second reaction times. At Brightwell Contractors, we pride ourselves on our lightning-fast reaction times in letting the relevant officials know as soon as one of our alarm systems goes off.</p>
  </article>
  <div class="pill__photo" style="left:399px;top:666px;background:linear-gradient(135deg,#f4f4f4,#e3e3e3)" role="img" aria-label="Hand touching a white motion sensor"></div>

  <article class="pill pill--left" style="left:130px;top:789px;width:376px">
    <h3 class="pill__title">SURVEILLANCE</h3>
    <p class="pill__body">Owning a business is expensive, and leaving it unattended every night is a huge risk. This is why we at Brightwell Contractors believe that owning one of our CCTV or IP camera systems is a great way to monitor the safety of your business and your staff 24 hours a day.</p>
  </article>
  <div class="pill__photo" style="left:58px;top:775px;background:linear-gradient(135deg,#c9b48a,#5f6f86 55%,#dfe3e8)" role="img" aria-label="Dome security camera in a warehouse"></div>

  <article class="pill pill--right" style="left:53px;top:904px;width:384px">
    <h3 class="pill__title">ELECTRICAL SERVICES</h3>
    <p class="pill__body">To remain the one-stop-shop that we strive to be for our customers, Brightwell Contractors Tech has a team of licensed Line Voltage Electricians. This team possess the ability to help our customers with a variety of projects and troubleshooting.</p>
  </article>
  <div class="pill__photo" style="left:399px;top:893px;background:linear-gradient(135deg,#8a8f96,#3b3f45 60%,#c9a23c)" role="img" aria-label="Electrician working on an electrical panel"></div>

  <div class="cta">LET US HELP YOU PROTECT<br>YOUR BUSINESS TODAY.</div>
  <div class="contact">
    <svg class="contact__slab" width="564" height="106" viewBox="0 0 564 106"><polygon points="329,0 564,0 564,106 295,106" fill="var(--black)"/></svg>
    <div class="contact__kicker" style="top:17px">CONTACT US</div>
    <div class="contact__phone" style="top:35px">
      <svg width="26" height="28" viewBox="0 0 24 24"><path fill="var(--ink)" d="M6.6 10.8a15.1 15.1 0 0 0 6.6 6.6l2.2-2.2c.3-.3.7-.4 1-.2 1.1.4 2.3.6 3.6.6.6 0 1 .4 1 1V20c0 .6-.4 1-1 1A17 17 0 0 1 3 4c0-.6.4-1 1-1h3.5c.6 0 1 .4 1 1 0 1.3.2 2.5.6 3.6.1.3 0 .7-.2 1z"/></svg>
      555-204-7390
    </div>
    <div class="contact__mail" style="top:74px">OFFICE@BWC-KMO.COM</div>
    <div class="badge-round" style="left:365px"></div>
    <div class="badge-square" style="left:450px"></div>
  </div>
</section>

</body>
</html>
```